Zielgruppe
Hersteller von Schreibwaren
ZG Jungen und Mädchen von 11 bis 18 Jahren, die Collegeblöcke nutzen
Aufgabenstellung
Markenadäquate Umsetzung
Aufmerksamkeitsstark und Differenzierend
auf relevanten Trends der Zielgruppe aufsetzen und nutzen

```html
<!DOCTYPE html>
<html lang="de">
<head>
<meta charset="utf-8">
<title>flower – be colorful · Collegeblock</title>
<link rel="stylesheet" href="https://fonts.googleapis.com/css2?family=Poppins:wght@600;700&family=Yellowtail&family=Caveat:wght@500&display=swap">
<style>
  :root {
    --page: #ffffff;
    --stage: #ece8e4;
    --ink-white: #ffffff;
    --green-light: #56c095;
    --green-mid: #38a866;
    --green-deep: #1f7a4a;
    --coral: #ee6f72;
    --violet: #7a4fb0;
    --violet-deep: #4e2f86;
  }
  * { box-sizing: border-box; margin: 0; padding: 0; }
  html, body { width: 891px; height: 1200px; overflow: hidden; background: var(--page); }
  .board { position: relative; width: 891px; height: 1200px; }

  .stage {
    position: absolute; width: 422px; height: 445px;
    background: var(--stage);
    display: flex; align-items: center; justify-content: center;
  }
  .stage--top { left: 405px; top: 119px; }
  .stage--bottom { left: 406px; top: 632px; }

  .cover {
    position: absolute; width: 315px; height: 445px; overflow: hidden;
    box-shadow: 0 2px 6px rgba(0,0,0,.18);
  }
  .cover--top { left: 65px; top: 119px; }
  .cover--bottom { left: 67px; top: 632px; }
  .stage .cover { position: relative; transform: scale(.84); box-shadow: 0 8px 18px rgba(0,0,0,.28); }

  .cover__art { position: absolute; inset: 0; }
  .cover--green .cover__art {
    background:
      radial-gradient(circle at 70% 40%, var(--green-light) 0, transparent 55%),
      linear-gradient(160deg, var(--green-mid) 0%, var(--green-light) 45%, var(--green-deep) 100%);
  }
  .cover--violet .cover__art {
    background:
      radial-gradient(circle at 55% 50%, var(--coral) 0, transparent 55%),
      linear-gradient(160deg, var(--violet) 0%, var(--coral) 50%, var(--violet-deep) 100%);
  }

  .brand {
    position: absolute; left: 59px; top: 70px;
    display: flex; align-items: center; gap: 6px;
    font-family: "Poppins", sans-serif; font-weight: 700;
    font-size: 20px; color: var(--ink-white);
  }
  .brand__square { width: 14px; height: 14px; background: var(--ink-white); }

  .title {
    position: absolute; left: 0; top: 0;
    font-family: "Poppins", sans-serif; font-weight: 700;
    color: var(--ink-white); line-height: 1; letter-spacing: -6px;
  }
  .title__line { position: absolute; white-space: nowrap; font-size: 150px; }
  .title__line--flo { left: 36px; top: 92px; }
  .title__line--wer { left: 46px; top: 178px; }

  .tagline {
    position: absolute; left: 60px; top: 322px;
    font-family: "Yellowtail", cursive; font-size: 27px;
    color: var(--ink-white); transform: rotate(-20deg); transform-origin: left center;
  }

  .ruling {
    position: absolute; left: 262px; top: 378px;
    width: 30px; height: 30px; border: 1.5px solid var(--ink-white);
  }
  .ruling__label {
    position: absolute; left: 248px; top: 410px;
    font-family: "Caveat", cursive; font-size: 20px; color: var(--ink-white);
    transform: rotate(-6deg);
  }
</style>
</head>
<body>
<main class="board">

  <article class="cover cover--green cover--top">
    <div class="cover__art" role="img" aria-label="Flat illustration of green leaves and colourful flowers"></div>
    <div class="brand"><span class="brand__square"></span>Fernwood</div>
    <h1 class="title"><span class="title__line title__line--flo">flo</span><span class="title__line title__line--wer">wer</span></h1>
    <p class="tagline">be colorful</p>
    <span class="ruling"></span><span class="ruling__label">kariert</span>
  </article>

  <section class="stage stage--top">
    <article class="cover cover--green">
      <div class="cover__art" role="img" aria-label="Flat illustration of green leaves and colourful flowers"></div>
      <div class="brand"><span class="brand__square"></span>Fernwood</div>
      <h2 class="title"><span class="title__line title__line--flo">flo</span><span class="title__line title__line--wer">wer</span></h2>
      <p class="tagline">be colorful</p>
      <span class="ruling"></span><span class="ruling__label">kariert</span>
    </article>
  </section>

  <article class="cover cover--violet cover--bottom">
    <div class="cover__art" role="img" aria-label="Flat illustration of purple leaves and colourful flowers on coral"></div>
    <div class="brand"><span class="brand__square"></span>Fernwood</div>
    <h2 class="title"><span class="title__line title__line--flo">flo</span><span class="title__line title__line--wer">wer</span></h2>
    <p class="tagline">be colorful</p>
    <span class="ruling"></span><span class="ruling__label">kariert</span>
  </article>

  <section class="stage stage--bottom">
    <article class="cover cover--violet">
      <div class="cover__art" role="img" aria-label="Flat illustration of purple leaves and colourful flowers on coral"></div>
      <div class="brand"><span class="brand__square"></span>Fernwood</div>
      <h2 class="title"><span class="title__line title__line--flo">flo</span><span class="title__line title__line--wer">wer</span></h2>
      <p class="tagline">be colorful</p>
      <span class="ruling"></span><span class="ruling__label">kariert</span>
    </article>
  </section>

</main>
</body>
</html>
```